New Business Card/Website Logo

We need a business card design for a new company based in Sydney. The company focuses mainly in construction in the field of form work and concreting. Attached is the logo being used already which can be used as a base for a new design, the current one is simply too bland and we are looking to spruce it up so it stands out and looks nicer. The logo would also be used on the website which is currently under construction. The attached image has the name, mobile and also the license number which needs to be there. The current email address on there can be removed and can be replaced with the website http://www.pillarvane.com.au, thanks!
Updates

Target Market(s)

Construction industry. Focusing on form work and concreting

Industry/Entity Type

Construction

Requirements
Must have
• License # on card along with website http://www.pillarvane.com.au and mobile phone number
Nice to have
• You have freedom with the design. The current design was a mock up done quite quickly. Please just keep in mind the target audience - construction, thanks.
Should not have
• the breezepost email address can be removed(refer picture) and replaced somewhere on the design with the website http://www.pillarvane.com.au

```html
<!DOCTYPE html>
<html lang="en">
<head>
<meta charset="utf-8">
<title>Pillarvane – Business Card</title>
<link rel="stylesheet" href="https://fonts.googleapis.com/css2?family=Montserrat:wght@600&family=Mulish:wght@400&display=swap">
<style>
  :root {
    --backdrop: #e6e4df;
    --card-yellow: #d8c625;
    --card-yellow-deep: #cbb91c;
    --ink: #2b2a22;
    --rule: #3a382c;
  }
  html, body {
    margin: 0;
    padding: 0;
    width: 1200px;
    height: 720px;
    overflow: hidden;
    background: var(--backdrop);
  }
  .canvas {
    position: relative;
    width: 1200px;
    height: 720px;
    display: flex;
    align-items: center;
    justify-content: center;
  }
  .business-card {
    position: relative;
    width: 820px;
    height: 500px;
    background: linear-gradient(160deg, var(--card-yellow) 0%, var(--card-yellow-deep) 100%);
    box-shadow: 0 10px 30px rgba(0, 0, 0, 0.18);
    box-sizing: border-box;
    padding: 150px 0 0 120px;
  }
  .brand {
    display: flex;
    align-items: center;
    gap: 18px;
  }
  .brand-square {
    width: 34px;
    height: 34px;
    background: var(--ink);
  }
  .brand-name {
    font-family: "Montserrat", sans-serif;
    font-weight: 600;
    font-size: 58px;
    letter-spacing: 2px;
    color: var(--ink);
    margin: 0;
    line-height: 1;
  }
  .contact {
    margin-top: 34px;
    font-family: "Mulish", sans-serif;
    font-weight: 400;
    font-size: 30px;
    color: var(--ink);
    line-height: 1.3;
  }
  .contact p {
    margin: 0;
  }
  .contact-rule {
    width: 270px;
    height: 2px;
    background: var(--rule);
    margin: 14px 0 16px;
    border: 0;
  }
</style>
</head>
<body>
  <main class="canvas">
    <article class="business-card">
      <header class="brand">
        <span class="brand-square" aria-hidden="true"></span>
        <h1 class="brand-name">PILLARVANE</h1>
      </header>
      <section class="contact">
        <p class="contact-licence">Licence: 318452c</p>
        <p class="contact-website">http://www.pillarvane.com.au</p>
        <hr class="contact-rule">
        <p class="contact-phone">Ph: 0400 555 218</p>
      </section>
    </article>
  </main>
</body>
</html>
```